'Sorry we missed you'/ 'How did we do'

I need a 'sorry we missed you' card, and a 'how did we do' card. I have attached a reference for existing cards, and have provided our current logo, and our social media header (van photo).
For the 'How did we do' flyer, I would like for this to have a QR code of our gradelark account 'Hollowmere Sprinklers Ltd', which has 0 reviews at the moment.
If looking for any clarifications please message, the tone of the flyers should be professional.
Flyer will be vertical A6 format.
Edit- for clarity, I want 2x variations. One for ‘sorry we missed you’ and another for ‘How did we do’ each with descriptions above.

```html
<!DOCTYPE html>
<html lang="en">
<head>
<meta charset="utf-8">
<title>Sorry We Missed You – Hollowmere Sprinklers</title>
<link href="https://fonts.googleapis.com/css2?family=Bebas+Neue&family=Fira+Sans:wght@400;500;600&display=swap" rel="stylesheet">
<style>
  :root {
    --backdrop: #939393;
    --paper: #ffffff;
    --brand-blue: #1b6bb5;
    --brand-orange: #f26a31;
    --ghost-blue: #e4edf6;
    --ink: #2b2b2b;
    --white: #ffffff;
  }
  * { margin: 0; padding: 0; box-sizing: border-box; }
  html, body {
    width: 1199px;
    height: 1200px;
    overflow: hidden;
    background: var(--backdrop);
  }
  .flyer {
    position: absolute;
    left: 224px;
    top: 71px;
    width: 750px;
    height: 1059px;
    background: var(--paper);
    overflow: hidden;
  }
  .flyer-shapes {
    position: absolute;
    inset: 0;
    width: 750px;
    height: 1059px;
  }
  .headline-ghost {
    font-family: "Bebas Neue", "Oswald", sans-serif;
    fill: var(--ghost-blue);
  }
  .brand {
    position: absolute;
    left: 400px;
    top: 150px;
    width: 340px;
    display: flex;
    align-items: center;
    justify-content: center;
    gap: 14px;
  }
  .brand-mark {
    width: 30px;
    height: 30px;
    background: var(--brand-blue);
  }
  .brand-name {
    font-family: "Fira Sans", sans-serif;
    font-weight: 500;
    font-size: 40px;
    color: var(--ink);
    letter-spacing: -0.5px;
  }
  .contact-panel {
    position: absolute;
    left: 395px;
    top: 387px;
    width: 355px;
    height: 495px;
    color: var(--white);
    font-family: "Fira Sans", sans-serif;
    text-align: center;
  }
  .contact-panel p {
    position: absolute;
    left: 0;
    width: 100%;
    font-size: 22.5px;
    line-height: 30.6px;
  }
  .contact-intro { top: 45px; padding: 0 30px; }
  .contact-address { top: 257px; }
  .contact-phone { top: 320px; font-weight: 600; font-size: 28px !important; }
  .contact-email { top: 386px; }
  .contact-web { top: 416px; font-weight: 600; }
  .missed-band {
    position: absolute;
    left: 0;
    top: 962px;
    width: 353px;
    height: 59px;
    background: var(--brand-orange);
    color: var(--white);
    font-family: "Bebas Neue", "Oswald", sans-serif;
    font-size: 62px;
    line-height: 63px;
    padding-left: 32px;
    white-space: nowrap;
  }
</style>
</head>
<body>
  <main class="flyer">
    <svg class="flyer-shapes" viewBox="0 0 750 1059" aria-hidden="true">
      <text class="headline-ghost" transform="translate(345,934) rotate(-90)" font-size="490" textLength="928" lengthAdjust="spacingAndGlyphs">SORRY</text>
      <polygon points="397,387 750,323 750,387" fill="var(--brand-orange)"/>
      <rect x="395" y="387" width="355" height="495" fill="var(--brand-blue)"/>
      <polygon points="397,882 750,882 750,947" fill="var(--brand-orange)"/>
    </svg>

    <div class="brand">
      <span class="brand-mark"></span>
      <span class="brand-name">Hollowmere</span>
    </div>

    <section class="contact-panel">
      <p class="contact-intro">For further information, please contact your landlord / letting agent directly. Alternatively, see our contact details below.</p>
      <p class="contact-address">14 Alder Quay Row,<br>Edinburgh EH7 4PX</p>
      <p class="contact-phone">0131 496 0318</p>
      <p class="contact-email">info@ hollowmere.scot</p>
      <p class="contact-web">www.hollowmere.scot</p>
    </section>

    <h1 class="missed-band">WE MISSED YOU</h1>
  </main>
</body>
</html>
```